Wholesale e-commerce website re-design

We are a wholesaler of African-made and African-themed products, and we're looking to update the look and feel of our website www.terramarketgoods.com to improve user experience. We'd like to have a cleaner homepage that keeps the product category menus (but simplifies them), allows certain products to be featured, and has a simple CTA box (something like "Login" for existing wholesale customers or "Start a Business" for new customers). The layout might be something along the lines of http://www.pinewillowwares.com/ except with a shopping cart featured at the top right. Our colors tend to be earth-toned, but the current color palate looks dated. Also see our blog.terramarketgoods.com page for themes and color ideas that are maybe more up-to-date. On our product pages, we want to feature the products more prominently and have simpler, cleaner Buy or Add buttons.

Other reference sites for inspiration: vastherbalcrate.com, cozykitchenry.com, http://www.pinewillowwares.com, http://mbelatraders.com/ http://orunesa.com/

Reason: We like many of the designs that have been submitted so far, but need more time to make our final choice.

Target Market(s)

Small wholesale customers, most have a small business or home-based business. Also some retail, so an option for retail customers to click at the top to see retail pricing would be nice

Industry/Entity Type

Wholesale

Number of Pages Required

3 page

Font styles to use
Sans Serif

Requirements
Must have
• Clean, clear design that highlights products and reduces friction to customer purchase. Should include one homepage, one product page, and one shopping cart page design. Works with all browser types and be mobile-friendly.
Nice to have
• Other color schemes that would look good with our logo (maybe different from colors chosen below).
Should not have
• Splash pages with special effects, Adobe flash, elements that slow down page load times or that only work well in certain browsers.

```html
<!DOCTYPE html>
<html lang="en">
<head>
<meta charset="utf-8">
<title>Terra Market – Wholesale Home</title>
<link rel="stylesheet" href="https://fonts.googleapis.com/css2?family=Roboto:wght@300;400;500;700&family=Oswald:wght@400;500&display=swap">
<style>
:root{
  --orange:#dc8a2e;
  --red:#c23b2b;
  --dark:#2b2b2b;
  --text:#555;
  --muted:#999;
  --line:#e4e4e4;
  --soft:#f6f6f6;
  --white:#fff;
}
*{box-sizing:border-box;margin:0;padding:0}
html,body{width:1200px;height:3696px;overflow:hidden}
body{font-family:'Roboto',sans-serif;color:var(--text);background:var(--white);position:relative;font-size:14px}
.abs{position:absolute}
a{color:inherit;text-decoration:none}
/* top bar */
.topbar{top:0;left:0;width:1200px;height:48px;background:var(--soft);border-bottom:1px solid var(--line);display:flex;align-items:center;justify-content:space-between;padding:0 40px;font-size:13px;color:#666}
.topbar nav{display:flex;gap:22px}
.topbar nav span::before{content:"";display:inline-block;width:7px;height:7px;background:var(--red);border-radius:50%;margin-right:7px;vertical-align:middle}
.topbar .acct{display:flex;gap:22px;color:var(--red)}
/* header */
.header{top:48px;left:0;width:1200px;height:132px}
.logo{left:40px;top:30px;display:flex;align-items:center;gap:10px}
.logo .mark{width:56px;height:56px;border-radius:50%;background:var(--red)}
.logo b{font-family:'Oswald',sans-serif;font-weight:500;font-size:24px;color:var(--red);letter-spacing:1px;line-height:1}
.catmenu{left:215px;top:16px;display:grid;grid-template-columns:repeat(5,128px);row-gap:10px;font-size:13px;color:var(--red)}
.catmenu span{border-left:1px solid var(--line);padding-left:10px}
.search{left:215px;top:88px;width:420px;height:34px;border:1px solid var(--line);display:flex;align-items:center;padding:0 12px;font-size:11px;color:var(--muted);letter-spacing:.5px}
.search svg{margin-left:auto}
.cart{left:960px;top:40px;display:flex;gap:14px;align-items:flex-start}
.cart b{display:block;color:var(--dark);font-size:14px}
.cart small{font-size:11px;color:var(--muted);line-height:1.4;display:block;width:150px}
/* hero */
.hero{top:180px;left:0;width:1200px;height:380px;background:linear-gradient(120deg,#6d4a33 0%,#a77b56 35%,#d9c2a3 60%,#8b5c3d 100%)}
.hero .tag{left:40px;top:100px;background:var(--orange);color:#fff;padding:14px 26px;font-family:'Oswald',sans-serif}
.hero .tag small{display:block;font-size:26px;letter-spacing:1px}
.hero .tag strong{display:block;font-size:60px;font-weight:500;line-height:1}
.hero .cta{left:40px;top:290px;color:#fff;font-size:14px;font-weight:500;letter-spacing:1px}
.hero .arr{top:20px;width:34px;height:34px;border-radius:50%;background:rgba(255,255,255,.85);display:flex;align-items:center;justify-content:center}
/* tiles */
.tile{width:600px}
.tile h2{position:absolute;font-family:'Oswald',sans-serif;font-weight:400;font-size:46px;color:#fff;letter-spacing:1px;line-height:1}
.btn{position:absolute;background:var(--orange);color:#fff;font-size:12px;font-weight:500;letter-spacing:1px;padding:12px 26px}
.signup{background:#fff;text-align:center}
.signup h3{font-family:'Oswald',sans-serif;font-weight:500;font-size:34px;color:var(--dark);margin-top:70px}
.signup p{font-size:13px;color:var(--muted);margin:16px auto 0;width:420px;line-height:1.5}
.signup form{display:flex;width:520px;margin:34px auto 0}
.signup .field{flex:1;height:40px;border:1px solid var(--line);text-align:left;padding:12px;font-size:12px;color:var(--muted)}
.signup .go{background:var(--red);color:#fff;font-size:12px;font-weight:500;padding:13px 22px}
/* arrivals */
.section-title{top:1830px;left:0;width:1200px;text-align:center;color:var(--red);font-size:24px;font-weight:400}
.section-title::before,.section-title::after{content:"";display:inline-block;width:100px;height:1px;background:var(--red);vertical-align:middle;margin:0 20px}
.pager{top:1880px;right:40px;display:flex;gap:8px}
.pager span{width:28px;height:28px;border:1px solid var(--line);border-radius:50%;display:flex;align-items:center;justify-content:center}
.products{top:1925px;left:40px;display:grid;grid-template-columns:repeat(4,260px);gap:20px}
.card{border:1px solid var(--line);height:370px;position:relative;padding:16px}
.card .code{position:absolute;right:16px;top:12px;font-size:10px;color:var(--muted)}
.card .shot{height:170px;margin-top:20px;display:flex;justify-content:center}
.card .shot div{width:90px;height:170px}
.card h4{font-size:13px;font-weight:500;color:var(--dark);margin-top:14px}
.card .row{display:flex;align-items:center;justify-content:space-between;margin-top:10px}
.card .price{font-size:20px;font-weight:700;color:var(--dark)}
.qty{display:flex;border:1px solid var(--line);font-size:12px}
.qty span{width:24px;height:24px;display:flex;align-items:center;justify-content:center;border-left:1px solid var(--line)}
.qty span:first-child{border:0}
.card .add{position:static;display:inline-block;margin-top:18px}
/* features */
.features{top:2400px;left:0;width:1200px;height:290px;background:var(--soft);display:grid;grid-template-columns:repeat(3,1fr);padding:40px 40px 0}
.feature{text-align:center;padding:0 30px}
.feature h5{font-size:14px;font-weight:500;color:var(--dark);letter-spacing:1px;margin:14px 0 12px}
.feature p{font-size:13px;line-height:1.6;color:var(--muted)}
.feature .more{display:block;margin-top:12px;font-size:12px;color:var(--muted)}
/* about */
.about{top:2740px;left:0;width:1200px;height:420px;background:linear-gradient(180deg,#3a0f0a 0%,#8e2b16 55%,#e0742c 80%,#2a0d08 100%);text-align:center;color:#fff}
.about h2{display:inline-block;margin-top:20px;background:rgba(0,0,0,.35);padding:10px 60px;font-family:'Oswald',sans-serif;font-weight:400;font-size:34px;letter-spacing:2px}
.about p{width:980px;margin:40px auto 0;font-size:17px;line-height:1.8;font-weight:500}
.about .ghost{display:inline-block;margin-top:30px;border:1px solid #fff;padding:12px 34px;font-size:13px;letter-spacing:1px}
/* footer */
.footer{top:3185px;left:40px;width:1120px;display:grid;grid-template-columns:repeat(4,1fr);font-size:12px}
.footer h6{font-size:12px;font-weight:500;color:var(--dark);letter-spacing:1px;margin-bottom:12px}
.footer li{list-style:none;line-height:2;color:var(--muted)}
.footer li::before{content:"› ";color:var(--red)}
.footer address{font-style:normal;line-height:1.7;color:var(--muted)}
.footer-row{top:3535px;left:40px;width:1120px;display:grid;grid-template-columns:1.5fr 1fr 1.2fr;font-size:12px;border-top:1px solid var(--line);padding-top:20px}
.footer-row h6{font-size:12px;font-weight:500;color:var(--dark);letter-spacing:1px;margin-bottom:10px}
.mini{display:flex;margin-top:8px}
.mini .field{width:200px;height:32px;border:1px solid var(--line)}
.mini .go{background:var(--red);color:#fff;padding:9px 18px;font-size:11px}
.dots{display:flex;gap:8px}
.dots span{width:26px;height:26px;border-radius:50%;background:var(--red)}
.pay{display:flex;gap:8px;flex-wrap:wrap;width:260px}
.pay span{width:48px;height:30px;background:#e9e9e9;border:1px solid var(--line)}
.bottom{top:3660px;left:0;width:1200px;height:36px;background:var(--red);color:#fff;font-size:12px;text-align:center;line-height:36px}
</style>
</head>
<body>

<div class="abs topbar">
  <nav><span>About Africa</span><span>Quick Order</span><span>Retail Pricing</span><span>Help</span><span>Contact us</span></nav>
  <div class="acct"><span>Sign in</span><span>Register</span></div>
</div>

<header class="abs header">
  <div class="abs logo"><div class="mark"></div><b>TERRA<br>MARKET</b></div>
  <div class="abs catmenu">
    <span>African Clothing</span><span>African Home</span><span>African Clothing</span><span>African Clothing</span><span>African Clothing</span>
    <span>African Clothing</span><span>African Clothing</span><span>African Clothing</span><span>African Clothing</span><span>African Clothing</span>
  </div>
  <div class="abs search">KEYWORD SEARCH OR ITEM #
    <svg width="14" height="14" viewBox="0 0 14 14"><circle cx="6" cy="6" r="4.5" fill="none" stroke="#999" stroke-width="1.5"/><line x1="9.5" y1="9.5" x2="13" y2="13" stroke="#999" stroke-width="1.5"/></svg>
  </div>
  <div class="abs cart">
    <svg width="40" height="36" viewBox="0 0 40 36"><path d="M2 4h7l5 20h20l4-14H12" fill="none" stroke="#c23b2b" stroke-width="3"/><circle cx="16" cy="31" r="3" fill="#c23b2b"/><circle cx="31" cy="31" r="3" fill="#c23b2b"/></svg>
    <div><b>0 items</b><small>Your cart is empty. Start shopping to add items.</small></div>
  </div>
</header>

<section class="abs hero" role="img" aria-label="Bar soaps and spice bowls arranged on a wooden table">
  <div class="abs tag"><small>BAR SOAPS</small><strong>15% OFF</strong></div>
  <div class="abs cta">CLICK HERE TO SHOP NOW ›</div>
  <div class="abs arr" style="left:1100px"><svg width="10" height="10" viewBox="0 0 10 10"><path d="M7 1L3 5l4 4" fill="none" stroke="#333" stroke-width="1.5"/></svg></div>
  <div class="abs arr" style="left:1145px"><svg width="10" height="10" viewBox="0 0 10 10"><path d="M3 1l4 4-4 4" fill="none" stroke="#333" stroke-width="1.5"/></svg></div>
</section>

<section class="abs tile" style="top:560px;left:0;height:420px;background:linear-gradient(135deg,#3e2a1c,#7a5638 60%,#4a3222)" role="img" aria-label="Stacked raw African black soap bars">
  <h2 style="left:40px;top:300px">AFRICAN SOAPS</h2>
  <span class="btn" style="left:40px;top:360px">GO TO SOAPS</span>
</section>
<section class="abs tile" style="top:560px;left:600px;height:420px;background:linear-gradient(135deg,#c9b8d6,#8c6aa8 50%,#d7a25a)" role="img" aria-label="Amber essential oil bottles among lavender">
  <h2 style="left:30px;top:40px">ESSENTIAL OIL</h2>
  <span class="btn" style="left:30px;top:100px">GO TO SEE</span>
</section>

<section class="abs tile signup" style="top:980px;left:0;height:380px">
  <h3>SIGN UP FOR OUR PROMOTIONS!</h3>
  <p>Find new customers the best way with free promos and e-mail offers. You get new items each week!</p>
  <form><div class="field">Enter your email</div><span class="go">SIGN UP</span></form>
</section>
<section class="abs tile" style="top:980px;left:600px;height:380px;background:linear-gradient(135deg,#2b6f9c,#d9452e 40%,#e8b23a 70%,#2f7a4a)" role="img" aria-label="Colourful printed African fabrics folded in stacks">
  <h2 style="left:220px;top:240px">AFRICAN FABRICS</h2>
  <span class="btn" style="left:430px;top:300px">GO TO SEE</span>
</section>

<section class="abs tile" style="top:1360px;left:0;height:408px;background:linear-gradient(135deg,#2a1f18,#6b4a2e 50%,#3a2a1e)" role="img" aria-label="Carved wooden African sculptures on display">
  <h2 style="left:40px;top:30px">AFRICAN ARTWORK</h2>
  <span class="btn" style="left:240px;top:90px">GO TO SOAPS</span>
</section>
<section class="abs tile" style="top:1360px;left:600px;height:408px;background:linear-gradient(135deg,#e8e2da,#c9a98a 50%,#8b6244)" role="img" aria-label="Shea nuts and butter in a wooden bowl">
  <h2 style="left:30px;top:290px">HEALTH&amp;BEAUTY</h2>
  <span class="btn" style="left:30px;top:350px">GO TO SOAPS</span>
</section>

<h3 class="abs section-title">New Arrivals</h3>
<div class="abs pager"><span>‹</span><span>›</span></div>

<div class="abs products">
  <article class="card"><span class="code">Item Code - KA502</span><div class="shot"><div role="img" aria-label="Carved ebony drummer figurine" style="background:linear-gradient(#1a1a1a,#333)"></div></div><h4>Ebony Drummer - LG</h4><div class="row"><span class="price">9.95$</span><div class="qty"><span>1</span><span>–</span><span>+</span></div></div><span class="btn add">ADD TO CART</span></article>
  <article class="card"><span class="code">Item Code - KA502</span><div class="shot"><div role="img" aria-label="Amber bottle of body oil" style="background:linear-gradient(#6b3b12,#d07a2a)"></div></div><h4>Ebony Drummer - LG</h4><div class="row"><span class="price">9.95$</span><div class="qty"><span>1</span><span>–</span><span>+</span></div></div><span class="btn add">ADD TO CART</span></article>
  <article class="card"><span class="code">Item Code - KA502</span><div class="shot"><div role="img" aria-label="Carved ebony drummer figurine" style="background:linear-gradient(#1a1a1a,#333)"></div></div><h4>Ebony Drummer - LG</h4><div class="row"><span class="price">9.95$</span><div class="qty"><span>1</span><span>–</span><span>+</span></div></div><span class="btn add">ADD TO CART</span></article>
  <article class="card"><span class="code">Item Code - KA502</span><div class="shot"><div role="img" aria-label="Amber bottle of body oil" style="background:linear-gradient(#6b3b12,#d07a2a)"></div></div><h4>Ebony Drummer - LG</h4><div class="row"><span class="price">9.95$</span><div class="qty"><span>1</span><span>–</span><span>+</span></div></div><span class="btn add">ADD TO CART</span></article>
</div>

<section class="abs features">
  <div class="feature">
    <svg width="40" height="36" viewBox="0 0 40 36"><path d="M4 10l16-7 16 7v16l-16 7-16-7z M4 10l16 7 16-7 M20 17v16" fill="none" stroke="#c23b2b" stroke-width="2.5"/></svg>
    <h5>SAME DAY SHIPPING</h5>
    <p>Order before 2 PM (EST) to ship your order today! US mail orders will be shipped the same day before 11:30 AM.</p>
    <span class="more">Read more ›</span>
  </div>
  <div class="feature">
    <svg width="40" height="36" viewBox="0 0 40 36"><path d="M20 32S4 22 4 12a8 8 0 0116-2 8 8 0 0116 2c0 10-16 20-16 20z" fill="none" stroke="#c23b2b" stroke-width="2.5"/></svg>
    <h5>100% GUARANTEED</h5>
    <p>You are guaranteed to be 100% satisfied with anything that you order. If you are not happy you can return it for your choice of refund or exchange.</p>
    <span class="more">Read more ›</span>
  </div>
  <div class="feature">
    <svg width="40" height="36" viewBox="0 0 40 36"><rect x="4" y="8" width="32" height="22" rx="3" fill="none" stroke="#c23b2b" stroke-width="2.5"/><line x1="4" y1="15" x2="36" y2="15" stroke="#c23b2b" stroke-width="2.5"/></svg>
    <h5>BUY NOW PAY LATER</h5>
    <p>Order before 2 PM (EST) to ship your order today! US Mail orders will be shipped the same day before 11:30 AM.</p>
    <span class="more">Read more ›</span>
  </div>
</section>

<section class="abs about" role="img" aria-label="Sunset over the savanna with a lone acacia tree">
  <h2>ABOUT US</h2>
  <p>The business was started in 1998. For the first year, the business was operated by the founder Daniel Okoro, his family, and by one office person. Most of this period of time was spent learning about the market for African goods, and developing a base of reliable suppliers.</p>
  <span class="ghost">READ MORE</span>
</section>

<footer class="abs footer">
  <div><h6>CUSTOMER HELP</h6><ul><li>Catalogs</li><li>African Stores Near You</li><li>FAQs</li><li>Shipping Policies</li><li>Retail Pricing</li></ul></div>
  <div><h6>BUSINESS TOOLS</h6><ul><li>Catalogs</li><li>African Stores Near You</li><li>FAQs</li><li>Shipping Policies</li><li>Retail Pricing</li></ul></div>
  <div><h6>MORE ABOUT AFRICA</h6><ul><li>Catalogs</li><li>African Stores Near You</li><li>FAQs</li><li>Shipping Policies</li><li>Retail Pricing</li></ul></div>
  <div><h6>CONTACT INFO</h6><address>Tel: (555) 014-2210<br>Fax: (555) 014-2299<br>Email: hello@terramarketgoods.com<br>118 Cedar Row, Brookhaven, NY<br>Business Hours: 9 AM to 5 PM EST<br>Mon-Fri, and 9 AM to 2 PM Saturday</address></div>
</footer>

<div class="abs footer-row">
  <div><h6>NEWSLETTER</h6><span style="color:#999">Subscribe to get news</span><div class="mini"><div class="field"></div><span class="go">SIGN UP</span></div></div>
  <div><h6>SOCIAL</h6><div class="dots"><span></span><span></span><span></span><span></span></div></div>
  <div><h6>PAYMENT METHODS</h6><div class="pay"><span></span><span></span><span></span><span></span><span></span></div></div>
</div>

<div class="abs bottom">©1998-2015 Terra Market Imports. All rights reserved</div>

</body>
</html>
```